New doctor needs elegant, whimsical Business Card Design

CHALLENGE: how to highlight gynaecological service (use of abstract cervix in logo?) in NON-VULGAR way + project an elegant, professional tone?

We need a business card design (incl logo) for a gynaecologist who is starting his private practice. The main area of service will be colposcopy - a diagnostic procedure using a microscope to look at the tissues of the cervix for any potentially cancerous cells.

STYLE: Classic, elegant, timeless look. Fairly simple, not too cluttered. Logo NOT to overpower name. Want to project a professional but approachable image - "gentleman". Not too "corporate" - whimsical, without becoming feminine.

COLOUR: soft colours - no clashing primary colours, nothing too "brash" or commercial.
White background/black lettering + 1 colour accent, pattern repeated throughout card, in both logo & text (refer to "mock-up example" image file)
The colour accent should be BLUE: a serene/calm but confident shade: eg. strong pastel blue, dark baby blue (NOT royal blue, navy, turquoise, aquamarine, etc)

TEXT: have a calligraphy feel (but not too fancy as to be difficult to read at a glance) or more italics/rounded edges kind of font (refer to refer to "mock-up example" image file)
- Contrast between NAME in more italic font Vs. rest of text in "straight" print (or vice versa)

LOGO:
1) something very similar to "The Mira Pledge" logo (ref image attached) - an abstract, black line drawing of a woman's figure, with a single, coloured symbol. No detail in line drawing - NO head or arms - don't want it to be obviously women's figure - want it very stylised, abstract, fluid lines.

* The Mira Pledge used a heart but we would like to use an another symbol in BLUE - maybe an abstract of a cervix? eg. the "triangle" shape symbol (see the image file of the Bright Petal Wellness Initiative - the symbol in the middle of the flower) OR the "donut" representation of the cervix (see notes below)

BUT - don't want the symbol exactly over the groin area, otherwise looks vulgar. Don't want it to look like bikini or genitals! Symbol should be incorporated into line drawing but NOT drawing direct attention to the groin. Maybe displaced to one side? Or further up the body? Open to your ideas

2) We are also open to any other ideas you may have, of stylistic/abstract designs based on:
- the image of a cervix (looks very similar to a pink donut - usually shown in medical shorthand as a tiny circle in the middle of a bigger circle.)
- the cervix with some cells within ? Some stylised version of cancer cells?
(please see attached selection of images for reference/inspiration)

Target Market(s)

2 main audiences: women (18 - 70) concerned about abnormal PAP smear, other gynae-issues, 2) GP's referring their patients to a gynae-specialist

Industry/Entity Type

Medical

Requirements
Must have
• ONE side only - Reverse of business card must be kept blank for "Appointments" notes.

Should not have
• NO "retro" American feel - nor anything 60's or 70's kind of feel. Don't want fonts that look too commercial or industrial/harsh.

Logo: NO obvious silhouettes/profiles of women (abstract is OK but not detail), NO female reproductive system (2 ovaries & uterus), no female symbol - as these are the usual cliches for gynaecologists.

DON'T want the symbol exactly over the groin area, otherwise looks vulgar. Don't want it to look like bikini or genitals! Symbol should be incorporated into line drawing but NOT drawing direct attention to the groin. Maybe displaced to one side? Or further up the body? Open to your ideas

```html
<!DOCTYPE html>
<html lang="en">
<head>
<meta charset="utf-8">
<title>Dr Adrian Hale – Business Card</title>
<link rel="stylesheet" href="https://fonts.googleapis.com/css2?family=Lora:ital,wght@1,600&family=Montserrat:wght@600&family=Arimo:wght@400&display=swap">
<style>
  :root {
    --page: #ffffff;
    --blue: #4a8fc7;
    --blue-soft: #8ec2ea;
    --ink: #2b2b2b;
    --grey: #666666;
    --card-light: #ffffff;
    --card-dark-top: #5a5a5a;
    --card-dark-bottom: #000000;
    --on-dark: #ffffff;
    --on-dark-soft: #d8d8d8;
  }
  * { margin: 0; padding: 0; box-sizing: border-box; }
  html, body {
    width: 1200px; height: 350px; overflow: hidden;
    background: var(--page);
  }
  .stage { position: relative; width: 1200px; height: 350px; }

  .card {
    position: absolute; top: 10px;
    width: 508px; height: 292px;
    font-family: "Arimo", Arial, sans-serif;
    box-shadow: 0 14px 14px -10px rgba(0,0,0,0.28);
  }
  .card--light { left: 34px; background: var(--card-light); box-shadow: 0 14px 14px -10px rgba(0,0,0,0.28), 0 0 0 1px #eeeeee; }
  .card--dark { left: 660px; background: linear-gradient(180deg, var(--card-dark-top) 0%, #2a2a2a 45%, var(--card-dark-bottom) 100%); }

  .figure-art {
    position: absolute; left: 14px; top: 0;
    width: 150px; height: 292px;
    border-radius: 0 60px 60px 0 / 0 140px 140px 0;
  }
  .card--light .figure-art { background: linear-gradient(90deg, #f4f4f4, #e6e6e6 60%, #f7f7f7); }
  .card--dark .figure-art { background: linear-gradient(90deg, #4a4a4a, #5c5c5c 60%, #3a3a3a); }

  .name {
    position: absolute; left: 190px; top: 52px;
    font-family: "Lora", Georgia, serif; font-style: italic; font-weight: 600;
    font-size: 38px; line-height: 1;
    white-space: nowrap;
  }
  .card--light .name { color: var(--blue); }
  .card--dark .name { color: var(--on-dark); }

  .specialty {
    position: absolute; left: 190px; top: 96px;
    font-family: "Montserrat", Arial, sans-serif; font-weight: 600;
    font-size: 19px; line-height: 1;
  }
  .card--light .specialty { color: var(--ink); }
  .card--dark .specialty { color: var(--blue-soft); }

  .credentials {
    position: absolute; left: 190px; top: 121px;
    font-size: 12px; line-height: 1; white-space: nowrap;
  }
  .card--light .credentials { color: var(--grey); }
  .card--dark .credentials { color: var(--on-dark-soft); }

  .contacts { position: absolute; left: 166px; top: 171px; list-style: none; }
  .contacts li {
    display: flex; align-items: center; gap: 4px;
    height: 22px; font-size: 16px;
  }
  .card--light .contacts li { color: var(--ink); }
  .card--dark .contacts li { color: var(--on-dark); }
  .icon { width: 18px; height: 18px; flex: none; }

  .address {
    position: absolute; left: 188px; top: 243px;
    font-size: 15px; line-height: 17px; font-style: normal;
  }
  .card--light .address { color: var(--grey); }
  .card--dark .address { color: var(--on-dark-soft); }
</style>
</head>
<body>
<div class="stage">

  <section class="card card--light">
    <div class="figure-art" role="img" aria-label="Abstract fluid line drawing of a torso with a small blue accent mark"></div>
    <h1 class="name">Dr Adrian Hale</h1>
    <p class="specialty">Gynaecologist</p>
    <p class="credentials">BM BCh, MA (Oxon),Dip Obs, Franzcog,MD</p>
    <ul class="contacts">
      <li><svg class="icon" viewBox="0 0 18 18" aria-hidden="true"><circle cx="9" cy="9" r="9" fill="var(--blue)"/><path d="M5.6 4.5l1.9-.4 1 2.4-1.2.9c.5 1.3 1.5 2.3 2.8 2.8l.9-1.2 2.4 1-.4 1.9c-4 .3-7.7-3.4-7.4-7.4z" fill="#fff"/></svg>+ 61 8 65550142</li>
      <li><svg class="icon" viewBox="0 0 18 18" aria-hidden="true"><circle cx="9" cy="9" r="9" fill="var(--blue)"/><rect x="6" y="4" width="6" height="3" fill="#fff"/><rect x="4" y="7.5" width="10" height="5" rx="1" fill="#fff"/><rect x="6" y="11" width="6" height="3" fill="#fff" stroke="var(--blue)" stroke-width=".6"/></svg>+ 61 8 65550187</li>
      <li><svg class="icon" viewBox="0 0 18 18" aria-hidden="true"><circle cx="9" cy="9" r="9" fill="var(--blue)"/><rect x="4" y="5.5" width="10" height="7" fill="#fff"/><path d="M4 5.5l5 4 5-4" fill="none" stroke="var(--blue)" stroke-width=".9"/></svg>admin@halegyn.com.au</li>
    </ul>
    <address class="address">Suite 12, Lakeview Medical Centre<br>40 Garden Ave, Westbury, Wa 6010</address>
  </section>

  <section class="card card--dark">
    <div class="figure-art" role="img" aria-label="Abstract fluid line drawing of a torso with a small blue accent mark"></div>
    <h2 class="name">Dr Adrian Hale</h2>
    <p class="specialty">Gynaecologist</p>
    <p class="credentials">BM BCh, MA (Oxon),Dip Obs, Franzcog,MD</p>
    <ul class="contacts">
      <li><svg class="icon" viewBox="0 0 18 18" aria-hidden="true"><circle cx="9" cy="9" r="9" fill="var(--blue)"/><path d="M5.6 4.5l1.9-.4 1 2.4-1.2.9c.5 1.3 1.5 2.3 2.8 2.8l.9-1.2 2.4 1-.4 1.9c-4 .3-7.7-3.4-7.4-7.4z" fill="#fff"/></svg>+ 61 8 65550142</li>
      <li><svg class="icon" viewBox="0 0 18 18" aria-hidden="true"><circle cx="9" cy="9" r="9" fill="var(--blue)"/><rect x="6" y="4" width="6" height="3" fill="#fff"/><rect x="4" y="7.5" width="10" height="5" rx="1" fill="#fff"/><rect x="6" y="11" width="6" height="3" fill="#fff" stroke="var(--blue)" stroke-width=".6"/></svg>+ 61 8 65550187</li>
      <li><svg class="icon" viewBox="0 0 18 18" aria-hidden="true"><circle cx="9" cy="9" r="9" fill="var(--blue)"/><rect x="4" y="5.5" width="10" height="7" fill="#fff"/><path d="M4 5.5l5 4 5-4" fill="none" stroke="var(--blue)" stroke-width=".9"/></svg>admin@halegyn.com.au</li>
    </ul>
    <address class="address">Suite 12, Lakeview Medical Centre<br>40 Garden Ave, Westbury, Wa 6010</address>
  </section>

</div>
</body>
</html>
```